Marks of Dunmore business card design

I need a clean, professional looking design using the attached logo with a bright green/ gray/dark gray/black colors. Maybe even an orange accent if it looks good. I am open to slight changes in the logo if needed. Details below on the info on what should be on the cards. We are a sign company in Ft. Lauderdale FL that specializes in yacht lettering on multi million dollar yachts.

Target Market(s)

marine industry, yachts

Industry/Entity Type

Business

Colors
9bcb3c
000000
606060
f37122

Requirements
Must have
• address: 2847 W. Harlow Rd.
• Harbor Vale, SC 33417
• Phone: 555-518-3046
• email/website: marksofdunmore@mailvista.net MarksofDunmore.net
Nice to have
• I would like it very clean and simple but professional looking. Nice layout and would prefer a darker background. Orange highlight only if it works.
Should not have
• Nothing fancy.

```html
<!DOCTYPE html>
<html lang="en">
<head>
<meta charset="utf-8">
<title>Marks of Dunmore — Business Card</title>
<link href="https://fonts.googleapis.com/css2?family=Work+Sans:wght@400;600&display=swap" rel="stylesheet">
<style>
  :root {
    --stage: #3a332f;
    --card: #1b1b1c;
    --card-edge: #2a2a2b;
    --accent-green: #1f8f3c;
    --logo-silver: #b9b9b9;
    --text-light: #c8c8c8;
    --text-muted: #9a9a9a;
    --rule: #555555;
  }
  * { box-sizing: border-box; margin: 0; padding: 0; }
  html, body {
    width: 1200px; height: 715px; overflow: hidden;
    background: var(--stage);
    font-family: "Work Sans", Arial, sans-serif;
  }
  .canvas {
    width: 1200px; height: 715px;
    display: flex; align-items: center; justify-content: center; gap: 50px;
  }
  .card {
    width: 525px; height: 300px;
    background: var(--card);
    border: 1px solid var(--card-edge);
    border-radius: 6px;
    position: relative;
    box-shadow: 0 18px 40px rgba(0,0,0,.45);
  }
  .card--front { border-bottom: 5px solid var(--accent-green); }
  .brand-name {
    font-weight: 600;
    color: var(--logo-silver);
    letter-spacing: .5px;
    white-space: nowrap;
  }
  .card--front .brand-name {
    position: absolute; left: 50%; top: 50%;
    transform: translate(-50%, -50%);
    font-size: 40px;
  }
  .card--back .brand-name {
    position: absolute; left: 40px; top: 104px;
    font-size: 23px;
  }
  .divider {
    position: absolute; left: 270px; top: 92px;
    width: 1px; height: 98px; background: var(--rule);
  }
  .contact-block {
    position: absolute; left: 290px; top: 92px;
    color: var(--text-light);
  }
  .person-name {
    font-size: 19px; font-weight: 400; letter-spacing: 2px; text-transform: uppercase;
  }
  .person-title { font-size: 11px; color: var(--text-muted); margin: 3px 0 12px; }
  .contact-list { list-style: none; font-size: 11.5px; line-height: 1.55; }
  .contact-list li { display: flex; align-items: center; gap: 7px; }
  .contact-list svg { width: 8px; height: 8px; fill: var(--text-muted); flex: none; }
  .contact-list .icon-mail { fill: none; stroke: var(--text-muted); stroke-width: 1.4; }
  .location {
    position: absolute; left: 40px; bottom: 36px;
    font-size: 11.5px; color: var(--text-muted); letter-spacing: .3px;
  }
</style>
</head>
<body>
<main class="canvas">
  <section class="card card--front">
    <p class="brand-name">Marks of Dunmore</p>
  </section>

  <section class="card card--back">
    <p class="brand-name">Marks of Dunmore</p>
    <div class="divider"></div>
    <div class="contact-block">
      <h1 class="person-name">Daniel Avery</h1>
      <p class="person-title">Founder</p>
      <ul class="contact-list">
        <li><svg viewBox="0 0 10 10"><path d="M2 0h2l1 3-1.5 1a6 6 0 0 0 2.5 2.5L7 5l3 1v2c0 1-1 2-2 2A8 8 0 0 1 0 2c0-1 1-2 2-2z"/></svg>555-518-3046</li>
        <li><svg class="icon-mail" viewBox="0 0 10 10"><path d="M1 2.5h8v5H1z M1 2.5l4 3 4-3"/></svg>marksofdunmore@mailvista.net</li>
        <li><svg viewBox="0 0 10 10"><circle cx="5" cy="5" r="4.5"/></svg>www.MarksofDunmore.net</li>
      </ul>
    </div>
    <p class="location">Location: 2847 W. Harlow Rd. Harbor Vale, SC 33417</p>
  </section>
</main>
</body>
</html>
```